Quiet Otter non alcohol beer can design

We are after 3 label designs for a new non alcoholic beer company (Quiet Otter). The colours to be used would primarily be a soft pink, blue, and white. Each label would essentially call out one dominant colour and the other two incorporated. Base of the design fun and eye-catching but still a modern clean aesthetic. A guide would be a general tie-dye colour all over the can with bold writing of the style of beer in one of the contrasting colours. Our logo then featuring in one of the secondary colours.
Eg: combined pink, blue and white can with white being dominant pink beer style and blue logo. Colours alternated on other varieties.
The varieties of beer are (HAZY) (RADLER) and (IPA)
Updates
Hi all, thank-you for the many and varied designs. Some have really hit the brief. We will review all tomorrow and get back to you ASAP. Thanks again for the great work and effort.
Target Market(s)
outdoorsy/active/health conscious
Industry/Entity Type
Beverage
Look and feel
Each slider illustrates characteristics of the customer's brand and the style your logo design should communicate.

```html
<!DOCTYPE html>
<html lang="en">
<head>
<meta charset="utf-8">
<title>Quiet Otter – Non Alcoholic Beer Labels</title>
<link rel="stylesheet" href="https://fonts.googleapis.com/css2?family=Anton&family=Oswald:wght@600&family=Montserrat:wght@200&display=swap">
<style>
  :root {
    --bg: #ffffff;
    --white: #ffffff;
    --ink: #1c1c2a;
    --logo-blue: #3a6fd6;
    --ring-red: #e8646a;
    --hazy: #4a2a7a;
    --hazy-light: #c9b6ef;
    --radler: #1e3a8c;
    --radler-light: #f0c8e6;
    --ipa: #e5545c;
    --ipa-light: #f7cbd6;
  }
  * { box-sizing: border-box; margin: 0; padding: 0; }
  html, body {
    width: 1200px;
    height: 900px;
    overflow: hidden;
    background: var(--bg);
  }
  .range {
    position: relative;
    width: 1200px;
    height: 900px;
    display: flex;
    justify-content: center;
    align-items: center;
    gap: 80px;
  }
  .label {
    position: relative;
    width: 280px;
    height: 740px;
    overflow: hidden;
    display: flex;
    flex-direction: column;
    align-items: center;
    color: var(--accent);
  }
  .label--hazy   { --accent: var(--hazy);   --accent-soft: #7b4bb8; }
  .label--radler { --accent: var(--radler); --accent-soft: #3b5fc4; }
  .label--ipa    { --accent: var(--ipa);    --accent-soft: #f08a8f; }

  .label__swirl {
    position: absolute;
    inset: 0;
    z-index: 0;
  }
  .label--hazy .label__swirl {
    background: radial-gradient(circle at 30% 20%, #e9dcf8 0%, transparent 45%),
                radial-gradient(circle at 75% 65%, #f3c9e4 0%, transparent 50%),
                linear-gradient(160deg, #cdb9f2 0%, #e6d2f5 50%, #c7b4ee 100%);
  }
  .label--radler .label__swirl {
    background: radial-gradient(circle at 10% 25%, #c9eef6 0%, transparent 35%),
                radial-gradient(circle at 80% 70%, #e9c5ec 0%, transparent 50%),
                linear-gradient(160deg, #f4e4f6 0%, #f7d4ea 50%, #e7c8ee 100%);
  }
  .label--ipa .label__swirl {
    background: radial-gradient(circle at 80% 15%, #fbe3ea 0%, transparent 45%),
                radial-gradient(circle at 25% 75%, #f4b9ca 0%, transparent 50%),
                linear-gradient(160deg, #f8d3dc 0%, #fbeef1 50%, #f5c5d2 100%);
  }

  .badge {
    position: relative;
    z-index: 1;
    margin-top: 44px;
    width: 262px;
    height: 262px;
    border-radius: 50%;
    border: 2px solid var(--ink);
    box-shadow: 0 0 0 3px rgba(255,255,255,0.8), 0 0 0 5px var(--ring-red);
    background: rgba(255,255,255,0.55);
    display: flex;
    flex-direction: column;
    align-items: center;
  }
  .badge__name {
    margin-top: 24px;
    font-family: "Oswald", sans-serif;
    font-weight: 600;
    font-size: 30px;
    letter-spacing: 1px;
    text-transform: uppercase;
    color: var(--logo-blue);
    line-height: 1;
  }
  .badge__mascot {
    margin-top: 14px;
    width: 150px;
    height: 170px;
    border-radius: 48% 48% 40% 40%;
    background: linear-gradient(100deg, #3f6fd8 0%, #6a82d8 45%, #e3948c 60%, #e8a595 100%);
    opacity: 0.9;
  }

  .style {
    position: relative;
    z-index: 1;
    margin-top: 50px;
    font-family: "Anton", sans-serif;
    font-size: 116px;
    line-height: 1;
    letter-spacing: -1px;
    color: var(--accent);
    -webkit-text-stroke: 0;
    text-shadow:
      4px 0 0 var(--white), -4px 0 0 var(--white),
      0 4px 0 var(--white), 0 -4px 0 var(--white),
      3px 3px 0 var(--white), -3px -3px 0 var(--white),
      3px -3px 0 var(--white), -3px 3px 0 var(--white);
    white-space: nowrap;
  }
  .label--radler .style { font-size: 112px; }
  .label--ipa .style { color: var(--ipa); }

  .beer {
    position: relative;
    z-index: 1;
    margin-top: 2px;
    font-family: "Montserrat", sans-serif;
    font-weight: 200;
    font-size: 56px;
    line-height: 1;
    letter-spacing: 20px;
    margin-right: -20px;
    color: var(--accent-soft);
    text-shadow:
      2px 0 0 var(--white), -2px 0 0 var(--white),
      0 2px 0 var(--white), 0 -2px 0 var(--white);
  }
  .label--hazy .beer { color: var(--hazy); }
  .label--radler .beer { color: #3452b8; }
  .label--ipa .beer { color: var(--ipa); }

  .abv {
    position: relative;
    z-index: 1;
    margin-top: 10px;
    font-family: "Oswald", sans-serif;
    font-weight: 600;
    font-size: 22px;
    letter-spacing: 0.5px;
    color: var(--accent);
    text-transform: uppercase;
  }
  .label--ipa .abv { color: var(--ipa); }
</style>
</head>
<body>
<main class="range">

  <section class="label label--hazy">
    <div class="label__swirl" role="img" aria-label="Soft lilac and pink tie-dye swirl pattern"></div>
    <div class="badge">
      <p class="badge__name">Quiet Otter</p>
      <div class="badge__mascot" role="img" aria-label="Brand mascot illustration in blue and salmon pink"></div>
    </div>
    <h2 class="style">HAZY</h2>
    <p class="beer">BEER</p>
    <p class="abv">Non Alcoholic</p>
  </section>

  <section class="label label--radler">
    <div class="label__swirl" role="img" aria-label="Pastel pink, lilac and aqua tie-dye swirl pattern"></div>
    <div class="badge">
      <p class="badge__name">Quiet Otter</p>
      <div class="badge__mascot" role="img" aria-label="Brand mascot illustration in blue and salmon pink"></div>
    </div>
    <h2 class="style">RADLER</h2>
    <p class="beer">BEER</p>
    <p class="abv">Non Alcoholic</p>
  </section>

  <section class="label label--ipa">
    <div class="label__swirl" role="img" aria-label="Soft pink and white tie-dye swirl pattern"></div>
    <div class="badge">
      <p class="badge__name">Quiet Otter</p>
      <div class="badge__mascot" role="img" aria-label="Brand mascot illustration in blue and salmon pink"></div>
    </div>
    <h2 class="style">IPA</h2>
    <p class="beer">BEER</p>
    <p class="abv">Non Alcoholic</p>
  </section>

</main>
</body>
</html>
```